Motivational Poster Design Project

I would like to create a poster with some of my favorite quotes to hang in my office. I did a similar project in 2012 and I've uploaded the top 2 designs so you can get a better idea of what I'm looking for. I will provide feedback on your design within 24 hours of receiving it.

The poster must contain the following quotes:

"You’re only given a little spark of madness. You mustn’t lose it.”
- Dorian Halbrook

“The most contrarian thing of all is not to oppose the crowd but to think for yourself.”
- Marcus Vell

"I constantly see people rise in life who are not the smartest, sometimes not even the most diligent, but they are learning machines. They go to bed every night a little wiser than they were when they got up and boy does that help, particularly when you have a long run ahead of you."
- Walter Brisco

“In theory, there’s no difference between theory and practice. But, in practice, there is.”
- Piet R. K. Ter Wolvenkamp

"At the end of the day, a reactionary life is a normal life. One thing is consistent in every remarkable person: they decide to do something remarkable. Don’t let the world choose who you become."
- Ravindra Kolpe

“It usually takes 3-4 months to try enough that you can do a proper 80/20 analysis, then two months to design systems to scale what *is* working.”
-Gus Ambery

“Authority is 20 percent given, 80 percent taken.”
- Harold Quimsby

“Your actions are consistent with the way the world occurs to you.”
- Anselm Grottke

Project Deadline Extended
Reason: I am going to be travelling with no access to internet until January 5th, 2015. I am extending the project deadline until 12/31/14 and I'll make a final decision during the 1st week of January.

Target Market(s)

Personal Project

Industry/Entity Type

Learning

Requirements
Must have
• The poster will be 24" high x 36" long and printed on canvas, so the image you create needs to have a resolution of at least 2700 x 3900.
Nice to have
• I don't have an exact vision for how the poster should look, so I am totally open to you using your creativity to develop, arrange and present the content as you'd like.
• That said, I would like an image (photo or posterized image) of the person being quoted along with each quote. I do not have specific images that I would like you to use, so you will need to find the images on your own. The images don't need to be perfect... I am more interested in the poster relating the essence of the quotes and the people being quoted than I am in perfect photographic images of the people being quoted.

```html
<!DOCTYPE html>
<html lang="en">
<head>
<meta charset="utf-8">
<title>Quotes Poster</title>
<link href="https://fonts.googleapis.com/css2?family=Josefin+Sans:wght@400;600&display=swap" rel="stylesheet">
<style>
  :root {
    --ink: #161a26;
    --rule: #1d2130;
    --portrait: #1a1c24;
    --bg-top: #b9bcdc;
    --bg-upper: #c4d4ea;
    --bg-mid: #c8f0ef;
    --bg-lower: #b7dfe6;
    --bg-bottom: #9a9db8;
  }
  * { margin: 0; padding: 0; box-sizing: border-box; }
  html, body { width: 900px; height: 1200px; overflow: hidden; }
  body {
    position: relative;
    font-family: "Josefin Sans", "Century Gothic", sans-serif;
    font-variant: small-caps;
    color: var(--ink);
    background: linear-gradient(180deg,
      var(--bg-top) 0%,
      var(--bg-upper) 22%,
      var(--bg-mid) 55%,
      var(--bg-lower) 75%,
      var(--bg-bottom) 100%);
  }
  .rule {
    position: absolute;
    left: 0;
    width: 900px;
    height: 3px;
    background: var(--rule);
  }
  .portrait {
    position: absolute;
    background: linear-gradient(160deg, #2a2d38, var(--portrait));
    border-radius: 4px;
  }
  .quote {
    position: absolute;
    font-size: 19px;
    line-height: 25px;
    letter-spacing: 0.6px;
  }
  .author {
    position: absolute;
    font-size: 19px;
    letter-spacing: 0.6px;
  }
</style>
</head>
<body>
  <!-- 1 -->
  <div class="portrait" role="img" aria-label="Posterized portrait of Dorian Halbrook" style="left:45px;top:2px;width:150px;height:121px;"></div>
  <p class="quote" style="left:228px;top:30px;width:560px;">“ You’re only given a little spark of madness. You mustn’t lose it. ”</p>
  <p class="author" style="left:228px;top:100px;">– Dorian Halbrook</p>
  <div class="rule" style="top:127px;"></div>

  <!-- 2 -->
  <p class="quote" style="left:65px;top:155px;width:680px;">“ The most contrarian thing of all is not to oppose the crowd but to think for yourself. ”</p>
  <p class="author" style="left:65px;top:229px;">– Marcus Vell</p>
  <div class="portrait" role="img" aria-label="Posterized portrait of Marcus Vell" style="left:762px;top:140px;width:84px;height:118px;"></div>
  <div class="rule" style="top:264px;"></div>

  <!-- 3 -->
  <div class="portrait" role="img" aria-label="Posterized portrait of Walter Brisco" style="left:80px;top:320px;width:100px;height:116px;"></div>
  <p class="quote" style="left:215px;top:273px;width:610px;">“ I constantly see people rise in life who are not the smartest, sometimes not even the most diligent, but they are learning machines. They go to bed every night a little wiser than they were when they got up and boy does that help, particularly when you have a long run ahead of you. ”</p>
  <p class="author" style="left:215px;top:416px;">– Walter Brisco</p>
  <div class="rule" style="top:455px;"></div>

  <!-- 4 -->
  <p class="quote" style="left:65px;top:479px;width:690px;">“ In theory, there’s no difference between theory and practice. But, in practice, there is. ”</p>
  <p class="author" style="left:65px;top:553px;">– Piet R. K. Ter Wolvenkamp</p>
  <div class="portrait" role="img" aria-label="Posterized portrait of Piet R. K. Ter Wolvenkamp" style="left:770px;top:465px;width:62px;height:115px;"></div>
  <div class="rule" style="top:584px;"></div>

  <!-- 5 -->
  <div class="portrait" role="img" aria-label="Posterized portrait of Ravindra Kolpe" style="left:95px;top:612px;width:75px;height:110px;"></div>
  <p class="quote" style="left:215px;top:598px;width:610px;">“ At the end of the day, a reactionary life is a normal life. One thing is consistent in every remarkable person: they decide to do something remarkable. Don’t let the world choose who you become. ”</p>
  <p class="author" style="left:215px;top:716px;">– Ravindra Kolpe</p>
  <div class="rule" style="top:744px;"></div>

  <!-- 6 -->
  <p class="quote" style="left:65px;top:776px;width:670px;">“ It usually takes 3–4 months to try enough that you can do a proper 80/20 analysis, then two months to design systems to scale what *is* working. ”</p>
  <p class="author" style="left:65px;top:873px;">-Gus Ambery</p>
  <div class="portrait" role="img" aria-label="Posterized portrait of Gus Ambery" style="left:765px;top:768px;width:80px;height:112px;border-radius:40px;"></div>
  <div class="rule" style="top:899px;"></div>

  <!-- 7 -->
  <div class="portrait" role="img" aria-label="Posterized portrait of Harold Quimsby" style="left:92px;top:910px;width:86px;height:143px;"></div>
  <p class="quote" style="left:235px;top:933px;width:580px;">“ Authority is 20 percent given, 80 percent taken. ”</p>
  <p class="author" style="left:222px;top:980px;">– Harold Quimsby</p>
  <div class="rule" style="top:1062px;"></div>

  <!-- 8 -->
  <p class="quote" style="left:65px;top:1089px;width:670px;">“ Your actions are consistent with the way the world occurs to you. ”</p>
  <p class="author" style="left:65px;top:1160px;">– Anselm Grottke</p>
  <div class="portrait" role="img" aria-label="Posterized portrait of Anselm Grottke" style="left:720px;top:1080px;width:135px;height:106px;"></div>
</body>
</html>
```